Franchise Power Point

Looking to add a strong design element to a very basic power point presentation about how to find the ideal franchise match. My website is www.brightpathventuring.com and www.vendalink/TKowalczyk

```html
<!DOCTYPE html>
<html lang="en">
<head>
<meta charset="utf-8">
<title>Franchise Presentation Slides</title>
<link href="https://fonts.googleapis.com/css2?family=Montserrat:wght@400;500&family=Playfair+Display:wght@700;800&display=swap" rel="stylesheet">
<style>
  :root {
    --backdrop: #a5b8d2;
    --navy: #132a40;
    --gold: #fcc419;
    --white: #ffffff;
    --ink: #0f2236;
  }
  * { margin: 0; padding: 0; box-sizing: border-box; }
  html, body {
    width: 1020px;
    height: 1200px;
    overflow: hidden;
    background: var(--backdrop);
  }
  .canvas {
    position: relative;
    width: 1020px;
    height: 1200px;
  }
  .slide {
    position: absolute;
    left: 66px;
    width: 887px;
    height: 499px;
    overflow: hidden;
  }

  /* Slide 1: key questions */
  .slide--questions { top: 73px; background: var(--navy); }
  .questions-header {
    position: absolute;
    left: 0; top: 0;
    width: 100%;
    height: 163px;
    background: var(--white);
    border-bottom: 7px solid var(--gold);
  }
  .questions-title {
    position: absolute;
    left: 91px;
    top: 22px;
    font-family: "Playfair Display", serif;
    font-weight: 800;
    font-size: 67px;
    line-height: 1;
    color: var(--ink);
    white-space: nowrap;
    letter-spacing: -0.5px;
  }
  .questions-title .accent { color: var(--gold); }
  .questions-subtitle {
    position: absolute;
    left: 0; width: 100%;
    top: 104px;
    text-align: center;
    padding-left: 10px;
    font-family: "Montserrat", sans-serif;
    font-weight: 400;
    font-size: 32px;
    line-height: 1;
    color: var(--ink);
  }
  .check-list {
    list-style: none;
    position: absolute;
    font-family: "Montserrat", sans-serif;
    font-weight: 400;
    color: var(--white);
  }
  .check-list li {
    position: absolute;
    left: 0;
    white-space: nowrap;
  }
  .check-list li svg {
    position: absolute;
    fill: none;
    stroke: var(--gold);
    stroke-width: 2.4;
    stroke-linecap: round;
    stroke-linejoin: round;
  }
  .questions-list {
    font-size: 19.5px;
    line-height: 22px;
  }
  .questions-list li { padding-left: 20px; }
  .questions-list li svg { left: 0; top: 4px; width: 13px; height: 11px; }
  .questions-list--left { left: 70px; top: 0; }
  .questions-list--right { left: 473px; top: 0; }

  /* Slide 2: research method */
  .slide--method { top: 632px; background: var(--navy); }
  .method-panel {
    position: absolute;
    left: 0; top: 0;
    width: 364px;
    height: 100%;
    background: var(--white);
  }
  .method-illustration {
    position: absolute;
    left: 81px;
    top: 59px;
    width: 203px;
    height: 176px;
    border-radius: 50%;
    background: radial-gradient(circle at 50% 50%, #e8eefb 0%, #dfe7f7 60%, #ffffff 72%);
  }
  .method-title {
    position: absolute;
    left: 47px;
    top: 242px;
    font-family: "Playfair Display", serif;
    font-weight: 700;
    font-size: 70px;
    line-height: 75px;
    color: var(--ink);
    letter-spacing: -0.5px;
  }
  .method-title .accent { color: var(--gold); display: block; }
  .method-list {
    left: 405px;
    top: 0;
    font-size: 17px;
    line-height: 20px;
  }
  .method-list li { padding-left: 17px; }
  .method-list li svg { left: 0; top: 3px; width: 12px; height: 11px; }
</style>
</head>
<body>
<main class="canvas">

  <section class="slide slide--questions" aria-label="Sample key questions slide">
    <header class="questions-header">
      <h1 class="questions-title"><span class="accent">Sample</span> Key Questions</h1>
      <p class="questions-subtitle">for the Educated Approach!</p>
    </header>

    <ul class="check-list questions-list questions-list--left">
      <li style="top:188px"><svg viewBox="0 0 13 11"><path d="M1 5.5 L4.8 9.5 L12 1"/></svg>Proper investment level</li>
      <li style="top:232px"><svg viewBox="0 0 13 11"><path d="M1 5.5 L4.8 9.5 L12 1"/></svg>Return goals – short, mid<br>and long term</li>
      <li style="top:299px"><svg viewBox="0 0 13 11"><path d="M1 5.5 L4.8 9.5 L12 1"/></svg>Skill set and background /<br>personality matching</li>
      <li style="top:365px"><svg viewBox="0 0 13 11"><path d="M1 5.5 L4.8 9.5 L12 1"/></svg>Employee profile: numbers<br>&amp; backgrounds</li>
      <li style="top:432px"><svg viewBox="0 0 13 11"><path d="M1 5.5 L4.8 9.5 L12 1"/></svg>Sales, marketing &amp; advertising</li>
    </ul>

    <ul class="check-list questions-list questions-list--right">
      <li style="top:188px"><svg viewBox="0 0 13 11"><path d="M1 5.5 L4.8 9.5 L12 1"/></svg>Concerns around the<br>Economy</li>
      <li style="top:254px"><svg viewBox="0 0 13 11"><path d="M1 5.5 L4.8 9.5 L12 1"/></svg>Need vs want</li>
      <li style="top:299px"><svg viewBox="0 0 13 11"><path d="M1 5.5 L4.8 9.5 L12 1"/></svg>Residual / Repeat /<br>Reoccurring Status</li>
      <li style="top:388px"><svg viewBox="0 0 13 11"><path d="M1 5.5 L4.8 9.5 L12 1"/></svg>B2B vs B2C</li>
      <li style="top:410px"><svg viewBox="0 0 13 11"><path d="M1 5.5 L4.8 9.5 L12 1"/></svg>Full time vs part time vs.<br>managed services</li>
    </ul>
  </section>

  <section class="slide slide--method" aria-label="The research method slide">
    <div class="method-panel">
      <div class="method-illustration" role="img" aria-label="Illustration of report documents with charts under a magnifying glass"></div>
      <h2 class="method-title">The<br>Research<span class="accent">Method</span></h2>
    </div>

    <ul class="check-list method-list">
      <li style="top:49px"><svg viewBox="0 0 12 11"><path d="M1 5.5 L4.5 9.5 L11 1"/></svg>Define your ideal match</li>
      <li style="top:87px"><svg viewBox="0 0 12 11"><path d="M1 5.5 L4.5 9.5 L11 1"/></svg>Establish contact with target franchisor</li>
      <li style="top:124px"><svg viewBox="0 0 12 11"><path d="M1 5.5 L4.5 9.5 L11 1"/></svg>Work through their standard process</li>
      <li style="top:162px"><svg viewBox="0 0 12 11"><path d="M1 5.5 L4.5 9.5 L11 1"/></svg>Review FDD</li>
      <li style="top:200px"><svg viewBox="0 0 12 11"><path d="M1 5.5 L4.5 9.5 L11 1"/></svg>Validate with franchisees</li>
      <li style="top:237px"><svg viewBox="0 0 12 11"><path d="M1 5.5 L4.5 9.5 L11 1"/></svg>Explore financing options</li>
      <li style="top:275px"><svg viewBox="0 0 12 11"><path d="M1 5.5 L4.5 9.5 L11 1"/></svg>Discuss territory</li>
      <li style="top:313px"><svg viewBox="0 0 12 11"><path d="M1 5.5 L4.5 9.5 L11 1"/></svg>Put together cash flow projections</li>
      <li style="top:350px"><svg viewBox="0 0 12 11"><path d="M1 5.5 L4.5 9.5 L11 1"/></svg>Attend Discovery Day</li>
      <li style="top:388px"><svg viewBox="0 0 12 11"><path d="M1 5.5 L4.5 9.5 L11 1"/></svg>Standard process</li>
      <li style="top:426px"><svg viewBox="0 0 12 11"><path d="M1 5.5 L4.5 9.5 L11 1"/></svg>Make a decision</li>
    </ul>
  </section>

</main>
</body>
</html>
```